New Consulting Firm News PowerPoint Template

We are a new consulting firm that specializes in Veltrix Unified Results Planning implementations in need of a new PowerPoint template. We need at least the following layouts:
• Main Cover Slide
• Agenda / Table of Contents
• Title slide for each of the agenda items leading into actual content
• Title + Content with nice bullets in the content
• Title + Sub-Title + Content with nice bullets in the content
• Title + Two Columns of Content
• Title + Sub-Title + Two Columns of Content
• Title + Three Columns of Content
• Title + Sub-Title + Three Columns of Content
• Title + Two Rows and Two Columns of Content (4 boxes)
• Title + Sub-Title + Two Rows and Two Columns of Content (4 boxes)
• Title + Blank
• Nascar Slide (Client logos arranged somehow)
• Case Study Slide
• Various infographic slides than can be used and modified would be amazing as well
Our logo has been uploaded and you can find our website here:
https://brankelladvisory.example
We would like the main theme colors to blend with our logo, but also have a variety of colors in the theme that compliment the main theme colors. Once we have selected a PowerPoint design we expect to immediately have a Word design contest and the winning PowerPoint design will likely be a heavy influence on the Word design.

Target Market(s)

CFO, CAO, VP of Finance, Controllers

Industry/Entity Type

Consulting

Font styles to use
Serif
Sans Serif

Requirements
Must have
• • Main Cover Slide
• Title + Blank
• Case Study Slide
Nice to have
• • Various infographic slides than can be used and modified would be amazing as well

```html
<!DOCTYPE html>
<html lang="en">
<head>
<meta charset="utf-8">
<title>Brankell Advisory – Presentation Template</title>
<link rel="stylesheet" href="https://fonts.googleapis.com/css2?family=Montserrat:wght@600;700;800&family=Open+Sans:wght@400;600&display=swap">
<style>
:root{
  --brand-blue:#1f6fc4;
  --brand-blue-deep:#18599f;
  --ink:#1d2533;
  --body-text:#5a6270;
  --rule:#c9d3de;
  --paper:#ffffff;
  --backdrop:#eceef1;
}
*{margin:0;padding:0;box-sizing:border-box}
html,body{width:773px;height:1200px;overflow:hidden}
body{background:var(--backdrop);position:relative;font-family:"Open Sans",Arial,sans-serif;color:var(--ink)}

.slide{position:absolute;background:var(--paper);overflow:hidden;box-shadow:0 2px 8px rgba(20,30,50,.18)}
.slide--cover{left:20px;top:20px;width:733px;height:564px}
.slide--two-col{left:20px;top:604px;width:356px;height:274px}
.slide--image-left{left:397px;top:604px;width:356px;height:274px}
.slide--three-col{left:208px;top:898px;width:356px;height:274px}

.photo{position:absolute}
.layer{position:absolute;inset:0;width:100%;height:100%}

/* cover */
.cover-photo{left:240px;top:0;right:0;bottom:0;
  background:linear-gradient(120deg,#e7ebef 0%,#c8ced6 30%,#f3f4f6 50%,#7d8797 72%,#2c3340 100%)}
.brand{position:absolute;left:40px;top:38px;display:flex;flex-direction:column;align-items:flex-start;gap:6px}
.brand__mark{width:30px;height:30px;background:var(--brand-blue)}
.brand__name{font-family:"Montserrat",Arial,sans-serif;font-weight:700;font-size:16px;color:var(--brand-blue);letter-spacing:.5px}
.cover-headline{position:absolute;left:40px;top:452px;font-family:"Montserrat",Arial,sans-serif;font-weight:800;font-size:27px;line-height:34px;color:#fff;letter-spacing:.3px}

/* content slides */
.slide-title{font-family:"Montserrat",Arial,sans-serif;font-weight:700;font-size:15px;color:var(--ink);text-align:center}
.copy{font-size:6px;line-height:8.5px;color:var(--body-text)}
.copy p+p{margin-top:5px}
.bullets{list-style:none;margin-top:6px}
.bullets li{font-size:6px;line-height:9px;color:var(--body-text);padding-left:8px;position:relative}
.bullets li::before{content:"";position:absolute;left:0;top:3px;width:4px;height:4px;background:var(--brand-blue)}

.slide--two-col .slide-title{position:absolute;top:18px;left:0;right:0}
.slide--two-col .columns{position:absolute;top:48px;left:22px;right:22px;display:grid;grid-template-columns:1fr 1fr;gap:18px}
.data-photo{left:0;right:0;bottom:0;height:118px;
  background:linear-gradient(100deg,#0d2b57 0%,#1c5aa5 40%,#6fa8e0 65%,#173f7a 100%)}

.city-photo{left:0;top:0;bottom:0;width:150px;
  background:linear-gradient(180deg,#e2e4e7 0%,#9a9ea5 45%,#4b4f56 80%,#2a2d32 100%)}
.slide--image-left .text-area{position:absolute;left:168px;right:18px;top:26px}
.slide--image-left .slide-title{text-align:left;margin-bottom:10px}

.desk-photo{left:0;right:0;top:0;height:128px;
  background:linear-gradient(110deg,#dfe6ee 0%,#9fb4cc 35%,#2e5f9c 60%,#0f2a50 100%)}
.slide--three-col .slide-title{position:absolute;top:134px;left:0;right:0}
.slide--three-col .columns{position:absolute;top:162px;left:20px;right:20px;display:grid;grid-template-columns:repeat(3,1fr);gap:12px}
</style>
</head>
<body>

<!-- Main cover -->
<section class="slide slide--cover">
  <div class="photo cover-photo" role="img" aria-label="Photo of business professionals in shirts reviewing documents together"></div>
  <svg class="layer" viewBox="0 0 733 564" preserveAspectRatio="none" aria-hidden="true">
    <polygon points="0,0 240,0 240,564 0,564" fill="#ffffff"/>
    <polygon points="0,255 733,500 733,564 0,564" fill="#ffffff"/>
    <polygon points="0,290 733,540 733,564 0,564" fill="var(--brand-blue)"/>
    <polygon points="240,0 290,0 240,60" fill="#ffffff"/>
  </svg>
  <div class="brand">
    <span class="brand__mark"></span>
    <span class="brand__name">BRANKELL ADVISORY</span>
  </div>
  <h1 class="cover-headline">INNOVATIVE EPM<br>SOLUTIONS FOR<br>FINANCE AND BEYOND:</h1>
</section>

<!-- Title + two columns -->
<section class="slide slide--two-col">
  <h2 class="slide-title">Slide Title</h2>
  <div class="columns">
    <div class="copy">
      <p>Our team aligns planning, close and reporting so finance leaders see results sooner and decide with confidence across every unit.</p>
      <p>We map current processes, design a clear model and guide each rollout step from first workshop to live use.</p>
    </div>
    <div class="copy">
      <p>Our team aligns planning, close and reporting so finance leaders see results sooner and decide with confidence across every unit.</p>
      <p>We map current processes, design a clear model and guide each rollout step from first workshop to live use.</p>
    </div>
  </div>
  <div class="photo data-photo" role="img" aria-label="Blue financial data visualisation with glowing charts"></div>
  <svg class="layer" viewBox="0 0 356 274" preserveAspectRatio="none" aria-hidden="true">
    <path d="M0,156 C120,190 240,150 356,176 L356,150 L0,150 Z" fill="#ffffff"/>
    <path d="M0,162 C120,196 240,156 356,182" fill="none" stroke="var(--rule)" stroke-width="1"/>
  </svg>
</section>

<!-- Image left + title + bullets -->
<section class="slide slide--image-left">
  <div class="photo city-photo" role="img" aria-label="Black and white photo of city skyscrapers"></div>
  <div class="text-area">
    <h2 class="slide-title">Slide Title</h2>
    <div class="copy">
      <p>Our team aligns planning, close and reporting so finance leaders see results sooner and decide with confidence across every unit.</p>
      <p>We map current processes, design a clear model and guide each rollout step from first workshop to live use.</p>
    </div>
    <ul class="bullets">
      <li>Faster monthly close</li>
      <li>Clear driver models</li>
      <li>Unified reporting</li>
      <li>Guided user training</li>
    </ul>
  </div>
</section>

<!-- Title + three columns -->
<section class="slide slide--three-col">
  <div class="photo desk-photo" role="img" aria-label="Photo of hands working on a laptop in blue light"></div>
  <svg class="layer" viewBox="0 0 356 274" preserveAspectRatio="none" aria-hidden="true">
    <path d="M0,100 C110,140 250,96 356,120 L356,274 L0,274 Z" fill="#ffffff"/>
    <path d="M0,94 C110,134 250,90 356,114" fill="none" stroke="var(--brand-blue)" stroke-width="1.5"/>
  </svg>
  <h2 class="slide-title">Slide Title</h2>
  <div class="columns">
    <div class="copy"><p>Our team aligns planning, close and reporting so finance leaders see results sooner and decide with confidence across every unit.</p></div>
    <div class="copy"><p>Our team aligns planning, close and reporting so finance leaders see results sooner and decide with confidence across every unit.</p></div>
    <div class="copy"><p>Our team aligns planning, close and reporting so finance leaders see results sooner and decide with confidence across every unit.</p></div>
  </div>
</section>

</body>
</html>
```